Business Card Design Project

We need a business card design for an existing company that we have just acquired and need to refresh and revamp to give it a fresher, more modern, and professional image.
We are a niche high end management consulting firm working with large BRQ300 type companies.
Our services include commercial advisory, change management, culture development, leadership and team development, and training.
The old website for this company is www.kelmorvo-grp.example that will give you a better understanding of what this business does.
However, we have updated the logo and are changing the website as well so your design for the business card might influence how we design the website.
Our corporate colours are red and white but we also use light grey, black, and dark blue (occasionally) on our stationery.
The final design should communicate partnership, creativity, performance, insight, and change.
Updates

Some of you were having trouble viewing the original logo file.  I have now updated another file with .jpg version of logo.  Hope this helps.

Target Market(s)

We are a consultancy firm servicing Top BRQ or Vantage 300 type companies.

Industry/Entity Type

Management Consulting

Requirements
Must have
• Design must have all contact information and logo on 1 side of card. Back of card should be solid colour or watermarked only - i.e. no real writing on back of card.
Cards must be scannable by those new business card scanners that store the image electronically.
Will be printing on high quality paper with matte finish so design must be high definition to allow good printing.
Card must be normal business card size (no small or 3/4 sized cards).
Nice to have
• A design that has a bit of 'movement' in it rather than look blockish and rigid. Not sure how this can be done but something that gives the card a sense of flow because our work all about integrating and synthesising the 'hard' commercial aspects with the 'soft' human (psychological) dimensions into contracts and projects.
Design should be transferrable to stationery and website to the extent possible/sensible.
Should not have
• - 'old fashioned' or 'girly' or 'comical' fonts.

- no clip art like images

- no superfluous design features that convey no real message or idea.

```html
<!DOCTYPE html>
<html lang="en">
<head>
<meta charset="utf-8">
<title>Kelmo Consulting Services – Business Card</title>
<link rel="stylesheet" href="https://fonts.googleapis.com/css2?family=Arimo:wght@400;700&family=Michroma&family=Open+Sans:wght@600;700&display=swap">
<style>
  :root {
    --stage: #3c434a;
    --brand-red: #b92027;
    --slate: #4b5661;
    --paper: #ffffff;
    --ink-soft: #3a3f44;
  }
  * { box-sizing: border-box; margin: 0; padding: 0; }
  html, body { width: 1200px; height: 900px; overflow: hidden; }
  body {
    background: var(--stage);
    position: relative;
    font-family: "Arimo", Arial, sans-serif;
  }
  .card-set {
    position: absolute;
    left: 147px;
    top: 308px;
    display: flex;
    gap: 25px;
  }
  .card {
    width: 440px;
    height: 283px;
    position: relative;
    overflow: hidden;
  }

  /* Front */
  .card--front { background: var(--paper); }
  .brand-row {
    position: absolute;
    left: 17px;
    top: 17px;
    display: flex;
    align-items: center;
    gap: 14px;
  }
  .brand-square {
    width: 78px;
    height: 78px;
    background: var(--brand-red);
    flex: none;
  }
  .brand-name {
    font-family: "Arimo", Arial, sans-serif;
    font-weight: 400;
    font-size: 23px;
    color: var(--brand-red);
    white-space: nowrap;
    letter-spacing: -0.2px;
  }
  .contact-list {
    position: absolute;
    left: 8px;
    top: 161px;
    width: 200px;
    list-style: none;
  }
  .contact-item {
    display: flex;
    align-items: center;
    height: 23px;
    margin-bottom: 7px;
  }
  .contact-icon {
    width: 30px;
    height: 23px;
    background: var(--brand-red);
    display: flex;
    align-items: center;
    justify-content: center;
    margin-right: 10px;
    flex: none;
  }
  .contact-text {
    font-family: "Michroma", sans-serif;
    font-size: 8.5px;
    color: var(--ink-soft);
    text-transform: uppercase;
    white-space: nowrap;
  }
  .name-plate {
    position: absolute;
    left: 214px;
    top: 160px;
    width: 226px;
    height: 85px;
    background: var(--slate);
    color: var(--paper);
    font-family: "Open Sans", sans-serif;
    font-weight: 700;
    font-size: 17px;
    line-height: 1.35;
    text-align: center;
    display: flex;
    flex-direction: column;
    justify-content: center;
    text-transform: uppercase;
  }

  /* Back */
  .card--back { background: var(--brand-red); }
  .emblem {
    position: absolute;
    left: 148px;
    top: 34px;
    width: 143px;
    height: 143px;
    background: var(--paper);
    display: flex;
    align-items: center;
    justify-content: center;
  }
  .emblem-name {
    font-family: "Arimo", Arial, sans-serif;
    font-weight: 400;
    font-size: 26px;
    color: var(--brand-red);
  }
  .divider {
    position: absolute;
    left: 0;
    top: 214px;
    width: 100%;
    height: 5px;
    background: var(--paper);
  }
  .slate-band {
    position: absolute;
    left: 0;
    top: 219px;
    width: 100%;
    height: 35px;
    background: var(--slate);
  }
</style>
</head>
<body>
  <main class="card-set">
    <section class="card card--front" aria-label="Card front">
      <div class="brand-row">
        <div class="brand-square"></div>
        <div class="brand-name">Kelmo Consulting Services</div>
      </div>

      <ul class="contact-list">
        <li class="contact-item">
          <span class="contact-icon">
            <svg width="18" height="12" viewBox="0 0 18 12" fill="none" stroke="#fff" stroke-width="1.2">
              <rect x="0.6" y="0.6" width="16.8" height="10.8"/>
              <path d="M0.6 0.6 L9 7 L17.4 0.6 M0.6 11.4 L7 5.5 M17.4 11.4 L11 5.5"/>
            </svg>
          </span>
          <span class="contact-text">rowan@kelmo.example</span>
        </li>
        <li class="contact-item">
          <span class="contact-icon">
            <svg width="16" height="16" viewBox="0 0 16 16" fill="none" stroke="#fff" stroke-width="1.2">
              <circle cx="8" cy="8" r="7"/>
              <ellipse cx="8" cy="8" rx="3" ry="7"/>
              <path d="M1 8 H15 M2.2 4.5 H13.8 M2.2 11.5 H13.8"/>
            </svg>
          </span>
          <span class="contact-text">www.kelmo.example</span>
        </li>
        <li class="contact-item">
          <span class="contact-icon">
            <svg width="16" height="16" viewBox="0 0 16 16" fill="none" stroke="#fff" stroke-width="1.3">
              <path d="M3 1.5 L5.5 1.5 L6.5 5 L4.8 6.3 C5.8 8.5 7.5 10.2 9.7 11.2 L11 9.5 L14.5 10.5 L14.5 13 C14.5 14 13.5 14.8 12.5 14.5 C7 13.3 2.7 9 1.5 3.5 C1.2 2.5 2 1.5 3 1.5 Z"/>
            </svg>
          </span>
          <span class="contact-text">(555) 010-2030</span>
        </li>
      </ul>

      <div class="name-plate">
        <span class="person-name">Rowan Ellery</span>
        <span class="person-role">Designer</span>
      </div>
    </section>

    <section class="card card--back" aria-label="Card back">
      <div class="emblem">
        <span class="emblem-name">Kelmo</span>
      </div>
      <div class="divider"></div>
      <div class="slate-band"></div>
    </section>
  </main>
</body>
</html>
```